A new website for Electrical Contractor Business

We are looking for a unique and new WordPress website design which would include 5 Pages - Home Page, Meet the Team, Our Services, Our Projects and Contact Us page.

The global theme for the website needs to be professional but simple to navigate as we cater for both business and home owner customers.

Our core business service is targeted around lighting from single room decorative to large office so the theme should incorporate this in some way.

The home page should include;
Our business logo, Contact number, Email address, small Image rotation box - Highlighting pervious projectsText box - With welcome message, chirpnet feed news reel/Customer feed back box.

I would also like to see a 2 boxes for the separate customer types we services. Business and Home Owner. each box will have a small image with a small text description with a link to the area of the services page relevant to that customer type.

Meet the team page -This will be introducing potential customers to the team so I would like it to include for each team member. Something like a small image and text area which will introduce an outline of the team members skills and abilities.

Our Services page This page will be outlining the different services on offer to the both customer types business and homeowner. Each service should have an image with text description of the service would good here.

Our projects page-Will include images of pervious projects and work we have completed along with a text area for the project description/ outliner.

Contact Us page - Should include a contact form which should include an option for the customer to quest us to call them back, also a selection box for them to inform us our how they found our details would be good.

Colour - The theme colours can be taken from the logo or feel free to impress with your own imagination.

Remember we are looking for a website that will interest our customers enough to except our services or be drawn further into the website.. So call to action links to other areas of the site/ contact page are welcome

Target Market(s)

Business - Office, warehousing and Large Store - lighting and Power
Home owner lighting and power

Coding

Coded - Design and coding required

Number of Pages Required

5+ page

Font styles to use
Serif
Sans Serif

Colors

Designer to choose colors to be used in the design.

Requirements
Must have
• Logo integrated into the website design - i.e. website colours which allow the logo to blend into the design.
Nice to have
• Custom but professional theme catering to business customers, but also show that we do provide services to home owners too.
Should not have
• Sorry am not interested in one oversized block image on rotation covering half the home page.. Images will be needed but not a single block over sized frame with not text, shape. Please use your imagination when considering this design

```html
<!DOCTYPE html>
<html lang="en">
<head>
<meta charset="utf-8">
<title>Brightwire Electrical</title>
<link href="https://fonts.googleapis.com/css2?family=Roboto:ital,wght@0,300;0,400;0,500;0,700;1,400&display=swap" rel="stylesheet">
<style>
:root{
  --navy:#1f2d52;
  --navy-deep:#16203c;
  --orange:#f26a2e;
  --ink:#2b2f3a;
  --muted:#7a7f8c;
  --light:#f3f4f7;
  --line:#e2e4ea;
  --white:#ffffff;
}
*{box-sizing:border-box;margin:0;padding:0}
html,body{width:1200px;height:4027px;overflow:hidden}
body{font-family:"Roboto",Arial,sans-serif;color:var(--ink);background:var(--white);position:relative}
a{color:inherit;text-decoration:none}
.wrap{width:960px;margin:0 auto;position:relative}

/* top bar */
.topbar{height:27px;background:var(--navy);color:#cfd5e6;font-size:10px}
.topbar .wrap{display:flex;justify-content:space-between;align-items:center;height:27px}
.topbar .call{background:var(--orange);color:#fff;height:27px;display:flex;align-items:center;padding:0 14px;letter-spacing:.5px}
.topbar .right{display:flex;gap:22px;align-items:center}
.topbar .social{display:flex;gap:8px;align-items:center}
.dot-icon{width:10px;height:10px;border-radius:50%;background:#cfd5e6;display:inline-block}

/* header */
.header{height:94px;background:var(--white);box-shadow:0 2px 6px rgba(0,0,0,.05)}
.header .wrap{display:flex;justify-content:space-between;align-items:center;height:94px}
.brand{display:flex;align-items:center;gap:10px;font-weight:700;font-size:16px;color:var(--navy);letter-spacing:1px}
.brand .mark{width:30px;height:30px;border-radius:50%;background:var(--orange)}
.nav{display:flex;align-items:center;gap:28px;font-size:10px;font-weight:500;color:var(--navy)}
.nav .active{color:var(--orange)}
.btn{display:inline-block;background:var(--orange);color:#fff;font-size:10px;font-weight:700;padding:9px 16px;border-radius:2px;letter-spacing:.5px}

/* hero */
.hero{height:341px;position:relative;background:linear-gradient(100deg,#0d1a33 0%,#27456e 45%,#5f7fa4 70%,#30465f 100%)}
.hero .copy{position:absolute;left:240px;top:72px;color:#fff;width:400px}
.hero h1{font-weight:300;font-size:30px;line-height:1.1}
.hero h1 strong{display:block;font-weight:700;font-size:44px}
.hero p{font-size:14px;margin:12px 0 22px;opacity:.9}

/* section title */
.title{text-align:center;font-size:17px;font-weight:400;color:var(--navy);letter-spacing:.5px}
.title strong{font-weight:700}
.title .orange{color:var(--orange)}
.divider{width:40px;height:2px;background:var(--orange);margin:8px auto 0}

/* welcome */
.welcome{height:384px;padding-top:52px}
.welcome-grid{display:flex;gap:40px;margin-top:46px}
.welcome-text{width:300px;font-size:10px;color:var(--muted);line-height:1.6}
.welcome-text .lead{font-size:11px;color:var(--ink);font-weight:500;margin-bottom:6px}
.ticks{list-style:none;margin-top:12px}
.ticks li{display:flex;align-items:center;gap:8px;margin-bottom:9px}
.ticks li::before{content:"";width:7px;height:7px;border-radius:50%;background:var(--orange)}
.features{display:grid;grid-template-columns:1fr 1fr;gap:34px 40px;flex:1}
.feature h3{font-size:11px;font-weight:500;color:var(--navy);display:flex;justify-content:space-between;align-items:center}
.feature p{font-size:9px;color:var(--muted);line-height:1.6;margin-top:10px;border-left:1px solid var(--line);padding-left:8px}

/* projects */
.projects-head{height:182px;background:var(--light);padding-top:44px}
.filters{display:flex;justify-content:center;gap:10px;margin-top:32px}
.filters span{font-size:9px;padding:8px 16px;border:1px solid #cfd2da;background:#fff;color:var(--ink)}
.filters .on{background:var(--orange);color:#fff;border-color:var(--orange)}
.project-grid{display:grid;grid-template-columns:repeat(4,300px);grid-auto-rows:298px}
.tile{position:relative}
.tile.overlay{background:linear-gradient(135deg,#1a1a1f,#3e3a36)}
.tile .label{position:absolute;left:20px;top:20px;right:20px;bottom:20px;border:1px solid rgba(255,255,255,.4);display:flex;flex-direction:column;align-items:center;justify-content:center;color:#fff;font-size:10px;letter-spacing:.5px;text-align:center;gap:10px}
.t1{background:linear-gradient(135deg,#7a6a55,#c9bfae)}
.t2{background:linear-gradient(135deg,#8d8f93,#d8d3ca)}
.t3{background:linear-gradient(135deg,#a7b8c6,#e2dfd6)}
.t4{background:linear-gradient(160deg,#3d4a78,#d98a6a)}
.t5{background:linear-gradient(135deg,#8aa3b3,#e0dbd2)}
.t6{background:linear-gradient(160deg,#3c4e6e,#7c8fa8)}
.t7{background:linear-gradient(135deg,#6b7b8f,#c7c0b6)}

/* services */
.services{height:757px;position:relative}
.services h2{position:absolute;left:160px;top:30px;font-size:30px;font-weight:400;color:var(--navy)}
.services h2 strong{font-weight:700}
.panel{position:absolute;width:600px;padding:40px 0 0 85px;color:#fff}
.panel.orange{left:0;top:94px;height:314px;background:var(--orange)}
.panel.navy{left:600px;top:408px;height:349px;background:var(--navy);padding-left:40px}
.panel .kicker{font-size:8px;font-weight:700;letter-spacing:.5px;border-left:2px solid #fff;padding-left:8px}
.panel .kicker span{display:block;font-size:15px;margin-top:2px}
.panel p{font-size:9px;line-height:1.6;width:330px;margin:10px 0 16px;opacity:.9}
.service-item{display:flex;gap:12px;align-items:flex-start;width:330px}
.service-item .box{width:34px;height:34px;border:1px solid rgba(255,255,255,.7);display:flex;align-items:center;justify-content:center;flex:none}
.service-item h4{font-size:10px;font-weight:500}
.service-item p{margin:4px 0 0;width:auto}
.btn-white{display:inline-block;background:#fff;color:var(--navy);font-size:9px;font-weight:700;padding:8px 14px;margin-top:20px}
.photo{position:absolute;width:600px}
.photo.p1{left:600px;top:0;height:408px;background:linear-gradient(160deg,#3c4e70,#c77f64 60%,#2d3650)}
.photo.p2{left:0;top:408px;height:349px;background:linear-gradient(135deg,#8aa0b0,#dcd5c8)}

/* testimonials */
.testimonials{height:425px;padding-top:70px;text-align:center;background:#fbfbfc}
.quote-mark{font-size:60px;color:#d9dbe2;line-height:.6;font-family:Georgia,serif}
.testimonials h2{font-size:23px;font-weight:500;color:var(--navy);margin-top:16px}
.testimonials blockquote{font-style:italic;font-size:12px;color:var(--muted);width:560px;margin:16px auto 0;line-height:1.6}
.author{font-size:11px;margin-top:14px;color:var(--ink)}
.author .stars{color:var(--orange);letter-spacing:1px}
.avatars{display:flex;justify-content:center;align-items:center;gap:10px;margin-top:24px}
.avatars span{width:26px;height:26px;border-radius:50%;background:#c7b9ab}
.avatars .big{width:44px;height:44px;border:3px solid #fff;box-shadow:0 0 0 1px var(--line)}

/* news */
.news{height:389px;padding-top:30px}
.news-grid{display:flex;justify-content:center;gap:22px;margin-top:38px}
.card{width:229px;background:#fff;box-shadow:0 2px 8px rgba(0,0,0,.08)}
.card .img{height:125px}
.card .i1{background:linear-gradient(135deg,#6d5a49,#c6ad8e)}
.card .i2{background:linear-gradient(135deg,#8a8d91,#d6d0c6)}
.card .i3{background:linear-gradient(135deg,#9fb2c2,#e0dcd3)}
.card .body{padding:14px 12px 16px}
.card h3{font-size:11px;font-weight:700;line-height:1.4}
.card p{font-size:8px;color:var(--muted);margin-top:8px;line-height:1.5}

/* quote */
.quote{height:537px;background:linear-gradient(90deg,#26282e 0%,#2e3138 60%,#3a3d44 100%);color:#fff;padding-top:56px}
.quote .title{color:#fff}
.quote .intro{font-size:9px;color:#bfc3cc;text-align:center;width:560px;margin:22px auto 0;line-height:1.7}
.quote-body{display:flex;align-items:center;margin-top:46px;padding-left:60px}
.call-block{width:240px;text-align:center}
.call-block .lbl{font-size:15px;margin-top:12px}
.call-block .num{font-size:27px;font-weight:500;margin:4px 0}
.call-block .sub{font-size:15px}
.or{width:90px;text-align:center;font-size:14px}
.quote-form{width:380px}
.row{display:flex;gap:20px;margin-bottom:16px}
.field{flex:1;height:32px;border:1px solid #5a5e67;font-size:8px;color:#aab0ba;padding:9px 8px}
.field.area{height:78px}
.quote-form .btn{display:block;width:110px;margin:10px auto 0;text-align:center}

/* footer */
.footer{height:214px;background:var(--navy-deep);color:#c9cfdd;padding-top:28px}
.footer-grid{display:flex;gap:44px}
.footer .brand{color:#fff;width:150px;border-right:1px solid #3a4566;height:90px}
.col h4{font-size:11px;color:#fff;font-weight:700;margin-bottom:10px}
.col a{display:block;font-size:9px;margin-bottom:7px}
.news-input{display:flex;width:230px;margin-top:4px}
.news-input span{flex:1;background:#fff;color:var(--muted);font-size:9px;padding:8px}
.news-input b{width:44px;background:var(--orange)}
.col small{font-size:7px;display:block;margin-top:6px}
.footer-bottom{display:flex;justify-content:space-between;align-items:center;margin-top:34px;font-size:9px}
.footer-bottom .social{display:flex;gap:8px}
.footer-bottom .social span{width:18px;height:18px;border-radius:50%;background:#3a4566}
</style>
</head>
<body>

<div class="topbar">
  <div class="wrap">
    <div class="call">CALL US : +1 555 010 2040</div>
    <div class="right">
      <span>EMAIL: hello@brightwire-electric.com</span>
      <span class="social">chirpnet <i class="dot-icon"></i><i class="dot-icon"></i><i class="dot-icon"></i></span>
    </div>
  </div>
</div>

<header class="header">
  <div class="wrap">
    <a class="brand" href="#"><span class="mark"></span>BRIGHTWIRE</a>
    <nav class="nav">
      <a class="active" href="#">HOME</a>
      <a href="#">MEET THE TEAM</a>
      <a href="#">OUR SERVICES</a>
      <a href="#">PROJECTS</a>
      <a href="#">CONTACT US</a>
      <a class="btn" href="#">GET A QUOTE</a>
    </nav>
  </div>
</header>

<section class="hero" role="img" aria-label="Electrician in hi-vis vest and hard hat looking over a city skyline at night">
  <div class="copy">
    <h1>Fast &amp; Reliable <strong>Electrical Services</strong></h1>
    <p>Vivamus ut dolor magna, facilisis convallis aliquam dolor, euismod id consectetur elit.</p>
    <a class="btn" href="#">GET A QUOTE</a>
  </div>
</section>

<section class="welcome">
  <h2 class="title">WELCOME TO <strong class="orange">BRIGHTWIRE ELECTRICAL</strong></h2>
  <div class="divider"></div>
  <div class="wrap welcome-grid">
    <div class="welcome-text">
      <p class="lead">Lorem ipsum dolor sit amet, consectetur adipiscing elit. Sed eget odio condimentum, suscipit elit nec, rutrum mauris.</p>
      <p>Lorem ipsum dolor sit amet consectetur adipiscing elit. Sed eget odio condimentum suscipit elit nec rutrum mauris sed tempus.</p>
      <ul class="ticks">
        <li>Morbi fermentum felis nec.</li>
        <li>Morbi fermentum felis nec gravida tempus.</li>
        <li>Morbi fermentum felis nec gravida.</li>
        <li>Lorem ipsum dolor sit amet</li>
        <li>Integer eu risus consequat</li>
      </ul>
    </div>
    <div class="features">
      <div class="feature"><h3>Residential Services <svg width="22" height="22" viewBox="0 0 22 22" fill="none" stroke="#f26a2e" stroke-width="1.3"><path d="M3 11 11 4l8 7M6 9v9h10V9"/></svg></h3><p>Dependable wiring and lighting for homes, from single rooms to full rewires.</p></div>
      <div class="feature"><h3>Commercial Services <svg width="22" height="22" viewBox="0 0 22 22" fill="none" stroke="#f26a2e" stroke-width="1.3"><rect x="4" y="4" width="14" height="15"/><path d="M8 8h2M12 8h2M8 12h2M12 12h2"/></svg></h3><p>Office, warehouse and large store lighting and power, planned and installed.</p></div>
      <div class="feature"><h3>Industrial Services <svg width="22" height="22" viewBox="0 0 22 22" fill="none" stroke="#f26a2e" stroke-width="1.3"><path d="M3 19V10l5 3V10l5 3V5h5v14z"/></svg></h3><p>Heavy duty power systems and maintenance for plants and production sites.</p></div>
      <div class="feature"><h3>Quick Support <svg width="22" height="22" viewBox="0 0 22 22" fill="none" stroke="#f26a2e" stroke-width="1.3"><circle cx="11" cy="11" r="8"/><path d="M11 6v5l3 2"/></svg></h3><p>Fast call-outs and round the clock help whenever the power goes down.</p></div>
    </div>
  </div>
</section>

<section class="projects-head">
  <h2 class="title">OUR <strong>LATEST PROJECTS</strong></h2>
  <div class="divider"></div>
  <div class="filters">
    <span class="on">All Projects</span><span>Residential Services</span><span>Commercial Services</span><span>Industrial Services</span>
  </div>
</section>
<section class="project-grid">
  <div class="tile overlay" role="img" aria-label="Electrician working on a panel in low light">
    <div class="label"><svg width="18" height="18" viewBox="0 0 18 18" fill="none" stroke="#fff" stroke-width="1.3"><path d="M9 3v12M3 9h12"/></svg>RESIDENTIAL SERVICE<br>INSTALLATION</div>
  </div>
  <div class="tile t1" role="img" aria-label="Electrician kneeling beside cable reels"></div>
  <div class="tile t2" role="img" aria-label="Electrician in hard hat at a control cabinet"></div>
  <div class="tile t3" role="img" aria-label="Two engineers inspecting an industrial site"></div>
  <div class="tile t4" role="img" aria-label="Worker in hi-vis vest at sunset over a refinery"></div>
  <div class="tile t5" role="img" aria-label="Electrician fitting a wall socket"></div>
  <div class="tile t6" role="img" aria-label="Engineer looking over a city at night"></div>
  <div class="tile t7" role="img" aria-label="Hands holding a meter and pliers at a switchboard"></div>
</section>

<section class="services">
  <h2>OUR <strong>SERVICES</strong></h2>
  <div class="panel orange">
    <div class="kicker">WORKING WITH EXCELLENT<span>OUR SPECIAL SERVICES</span></div>
    <p>Lorem ipsum dolor sit amet, consectetur adipiscing elit. Nunc et magna efficitur turpis venenatis bibendum nec eget ipsum.</p>
    <div class="service-item">
      <span class="box"><svg width="16" height="16" viewBox="0 0 16 16" fill="none" stroke="#fff" stroke-width="1.2"><path d="M2 14V7l4 2V7l4 2V3h4v11z"/></svg></span>
      <div><h4>Industrial Service</h4><p>Lorem ipsum dolor sit amet, consectetur adipiscing elit. Sed pretium nisl enim vel nulla euismod tincidunt.</p></div>
    </div>
    <a class="btn-white" href="#">READ MORE</a>
  </div>
  <div class="photo p1" role="img" aria-label="Worker in hi-vis vest facing an industrial skyline at dusk"></div>
  <div class="photo p2" role="img" aria-label="Electrician crouching to fit a wall outlet"></div>
  <div class="panel navy">
    <div class="kicker">WORKING WITH EXCELLENT<span>OUR SPECIAL SERVICES</span></div>
    <p>Lorem ipsum dolor sit amet, consectetur adipiscing elit. Nunc et magna efficitur turpis venenatis bibendum nec eget ipsum.</p>
    <div class="service-item">
      <span class="box"><svg width="16" height="16" viewBox="0 0 16 16" fill="none" stroke="#fff" stroke-width="1.2"><path d="M2 8 8 3l6 5M4 7v7h8V7"/></svg></span>
      <div><h4>Residential Service</h4><p>Lorem ipsum dolor sit amet, consectetur adipiscing elit. Sed pretium nisl enim vel nulla euismod tincidunt.</p></div>
    </div>
    <a class="btn-white" href="#">READ MORE</a>
  </div>
</section>

<section class="testimonials">
  <div class="quote-mark">&ldquo;</div>
  <h2>What People are Saying...</h2>
  <blockquote>Lorem ipsum dolor sit amet, consectetur adipiscing elit. Nunc et magna efficitur turpis venenatis bibendum nec eget ipsum. Aliquam a euismod neque. Cras a quam nulla. Suspendisse sit amet sagittis turpis.</blockquote>
  <p class="author">- Daniel Reyes &nbsp;<span class="stars">★★★★★</span></p>
  <div class="avatars">
    <span role="img" aria-label="Customer portrait"></span>
    <span class="big" role="img" aria-label="Customer portrait"></span>
    <span role="img" aria-label="Customer portrait"></span>
    <span role="img" aria-label="Customer portrait"></span>
  </div>
</section>

<section class="news">
  <h2 class="title">LATEST <strong>NEWS</strong></h2>
  <div class="divider"></div>
  <div class="news-grid">
    <article class="card"><div class="img i1" role="img" aria-label="Electrician working on ceiling wiring"></div><div class="body"><h3>Lorem ipsum dolor sit amet est consectetur adipiscing elit.</h3><p>Suspendisse sit amet sagittis turpis. Suspendisse potenti. Aliquam metus.</p></div></article>
    <article class="card"><div class="img i2" role="img" aria-label="Electrician with cable reels on site"></div><div class="body"><h3>Lorem ipsum dolor sit amet est consectetur adipiscing elit.</h3><p>Suspendisse sit amet sagittis turpis. Suspendisse potenti. Aliquam metus.</p></div></article>
    <article class="card"><div class="img i3" role="img" aria-label="Engineer checking a control cabinet"></div><div class="body"><h3>Lorem ipsum dolor sit amet est consectetur adipiscing elit.</h3><p>Suspendisse sit amet sagittis turpis. Suspendisse potenti. Aliquam metus.</p></div></article>
  </div>
</section>

<section class="quote">
  <h2 class="title">LET'S GET YOU <strong>FREE QUOTE</strong></h2>
  <div class="divider"></div>
  <p class="intro">Lorem ipsum dolor sit amet, consectetur adipiscing elit. Nunc et magna efficitur turpis venenatis bibendum nec eget ipsum. Aliquam a euismod neque. Cras a quam nulla. Suspendisse sit amet sagittis turpis.</p>
  <div class="quote-body">
    <div class="call-block">
      <svg width="30" height="30" viewBox="0 0 30 30" fill="none" stroke="#fff" stroke-width="1.4"><circle cx="15" cy="11" r="5"/><path d="M5 26c1-6 5-9 10-9s9 3 10 9M8 12a7 7 0 0 1 14 0"/></svg>
      <p class="lbl">Call our Friendly Team</p>
      <p class="num">+1 555 010 2040</p>
      <p class="sub">24/7 Emergency Service</p>
    </div>
    <div class="or">Or</div>
    <form class="quote-form">
      <div class="row"><div class="field">Full Name*</div><div class="field">Email*</div></div>
      <div class="row"><div class="field">Phone</div><div class="field">Address</div></div>
      <div class="field area">Your Project Description</div>
      <a class="btn" href="#">Get a Free Quote</a>
    </form>
  </div>
</section>

<footer class="footer">
  <div class="wrap">
    <div class="footer-grid">
      <div class="brand"><span class="mark"></span>BRIGHTWIRE</div>
      <div class="col"><h4>Useful Links</h4><a href="#">Services</a><a href="#">Portfolio</a><a href="#">Get a Quote</a></div>
      <div class="col"><h4>Company</h4><a href="#">Why Brightwire Electrical</a><a href="#">About Us</a><a href="#">Contact</a></div>
      <div class="col"><h4>Join Our Mailbox!</h4><div class="news-input"><span>Your email address</span><b></b></div><small>Subscribe to our newsletter to get the important news.</small></div>
    </div>
    <div class="footer-bottom">
      <span>Copyright © 2018 Brightwire Electrical &nbsp;|&nbsp; Privacy Policy</span>
      <span class="social"><span aria-label="chirpnet"></span><span></span><span></span><span></span></span>
    </div>
  </div>
</footer>

</body>
</html>
```